Movie Poster/DVD jacket for Short Documentary

I am a documentary filmmaker who just completed a project titled "Sister Marigold". Here is the logline (short description of the movie): "An Oklahoma family is ripped apart after their 15-year-old son brutally murders his older sister in 1974. Controversy swirls around the case after his parents decide to hire a prominent defense attorney to keep him out of jail." I have several good photos of the family involved. I am in the process of submitting the film to several festivals and I want a professional looking movie poster that can be sent with film submissions. The look needs to dramatic and serious.
Updates

Project Deadline Extended Reason: We just had several more submission enter today and need a few more days to evaluate. Thank you for you patience. Added Thursday, November 19, 2015

Target Market(s)

Film festivals, television

Industry/Entity Type

Movie

Colors
f04a50

Requirements
Must have
• the color red and have a similar appearance to the sample movie posters.
• Also, tagline: turning a blind eye into broken hearts
• Directors name: a film by Rob Haskett
Nice to have
• rough
Should not have
• Not a gruesome look.

```html
<!DOCTYPE html>
<html lang="en">
<head>
<meta charset="utf-8">
<title>Sister Marigold — a film by Rob Haskett</title>
<link rel="stylesheet" href="https://fonts.googleapis.com/css2?family=Open+Sans:wght@700;800&family=Old+Standard+TT:wght@400;700&display=swap">
<style>
  :root {
    --brand-red: #f04a50;
    --title-white: #ffffff;
    --parchment-light: #f1e2bd;
    --parchment-mid: #d9bf86;
    --parchment-dark: #9c7238;
    --ink-faded: rgba(70, 52, 34, 0.62);
    --ink-headline: rgba(85, 68, 48, 0.7);
    --photo-rust: #b5782e;
    --photo-amber: #d8a55a;
    --photo-deep: #8a4a1c;
  }
  * { margin: 0; padding: 0; box-sizing: border-box; }
  html, body {
    width: 776px;
    height: 1200px;
    overflow: hidden;
    background: var(--parchment-mid);
  }
  .poster {
    position: relative;
    width: 776px;
    height: 1200px;
    overflow: hidden;
    background:
      radial-gradient(ellipse at 45% 40%, var(--parchment-light) 0%, #e7d1a0 45%, var(--parchment-mid) 72%, var(--parchment-dark) 100%);
  }
  .title {
    position: absolute;
    font-family: "Open Sans", sans-serif;
    font-weight: 800;
    letter-spacing: -5px;
    line-height: 1;
  }
  .title-first {
    left: 30px;
    top: 2px;
    font-size: 150px;
    color: var(--brand-red);
  }
  .title-second {
    right: 22px;
    top: 104px;
    font-size: 112px;
    color: var(--title-white);
  }
  .credit {
    position: absolute;
    right: 26px;
    top: 212px;
    font-family: "Open Sans", sans-serif;
    font-weight: 700;
    font-size: 27px;
    letter-spacing: -0.5px;
    color: var(--brand-red);
  }
  .clipping {
    position: absolute;
    left: 40px;
    top: 228px;
    width: 440px;
    font-family: "Old Standard TT", serif;
  }
  .clipping-headline {
    font-weight: 700;
    font-size: 72px;
    line-height: 75px;
    color: var(--ink-headline);
    letter-spacing: 1px;
  }
  .clipping-byline {
    margin: 22px 0 6px 82px;
    font-size: 18px;
    color: var(--ink-faded);
  }
  .clipping-body p {
    font-size: 19px;
    line-height: 23px;
    color: var(--ink-faded);
    text-align: justify;
    text-indent: 22px;
    margin-bottom: 17px;
  }
  .photo-hoop {
    position: absolute;
    left: 360px;
    top: 520px;
    width: 420px;
    height: 680px;
    background:
      radial-gradient(ellipse at 45% 35%, rgba(216,165,90,0.55) 0%, rgba(181,120,46,0.55) 40%, rgba(138,74,28,0.25) 75%, transparent 100%),
      linear-gradient(180deg, rgba(181,120,46,0.15), rgba(138,74,28,0.45));
    mix-blend-mode: multiply;
  }
  .tagline {
    position: absolute;
    left: 0;
    right: 0;
    bottom: 12px;
    text-align: center;
    font-family: "Open Sans", sans-serif;
    font-weight: 700;
    font-size: 29px;
    letter-spacing: -0.8px;
    color: var(--brand-red);
    text-shadow: 0 0 3px #fff, 0 0 2px #fff, 0 0 6px rgba(255,255,255,0.7);
  }
</style>
</head>
<body>
  <main class="poster">
    <div class="clipping">
      <h2 class="clipping-headline">Teen held<br>in killing<br>of sister</h2>
      <p class="clipping-byline">By Dusty Marlow</p>
      <div class="clipping-body">
        <p>CEDAR FORD — "I just shot my sister. I need some help."</p>
        <p>Those were the words that rushed into the telephone late Wednesday when Deputy Ray Tolbert answered a call at the headquarters of the sheriff's office.</p>
        <p>Today a 15-year-old local High School sophomore was being held, accused of slaying his 20-year-old sister as a result of an argument over the noise the sister's two young daughters were making.</p>
        <p>Sheriff Wade Harlan said the shooting occurred apparently about 4:30 p.m. Wednesday at the rural home of Mr. and Mrs. Ben Marigold.</p>
        <p>Dead is Mrs. Robert Gates, 20, the Marigolds' daughter, who had come with her husband and children for a brief summer visit. They are from Millbrook.</p>
        <p>Held in the county jail without</p>
      </div>
    </div>

    <div class="photo-hoop" role="img" aria-label="Weathered sepia photograph of a backyard basketball hoop and pole"></div>

    <h1 class="title title-first">Sister</h1>
    <h1 class="title title-second">Marigold</h1>
    <p class="credit">a film by Rob Haskett</p>

    <p class="tagline">Turning a blind eye into broken hearts</p>
  </main>
</body>
</html>
```